Corporate Design für lumavent capital partners (lcp)
Zielgruppe
Was wir machen:
Wir sind ein hochwertiger Finanzmakler, der seinen Mandaten in allen Bereichen zum Thema 'Finanzen und Versicherungen' mit Rat und Tat zur Seite steht. Vertrauen und Seriosität stehen dabei an erster Stelle.
Unsere Dienstleistung zielt darauf ab, der Ansprechpartner Nummer 1 zu sein, wenn es um Produkte aus dem Finanz- und Versicherungssektor geht. Gemäß dem Motto 'Ihr Plan bis zum Schluss'.
Somit müssen sich unsere Mandanten nicht mit verschiedenen Banken und Versicherern auseinandersetzen und haben mit uns einen Ansprechpartner für alle Belange. Nach einer intensiven Anaylse der Ist-Situation erarbeiten wir im jeweiligen Bereich die optimale Lösung heraus und fassen diese schriftlich in einem Gesamtkonzept für unsere Mandanten zusammen. Somit erhält er eine übersichtliche Handlungsempfehlung von uns.
--> Kurz gesagt: Wir erstellen maßgeschneiderte Finanzkonzepte für Privatkunden, sowie für Klein- und Mittelständische Unternehmen.
Unsere Zielgruppe:
Da unsere Beratung fachlich und inhaltlich sehr anspruchsvoll ist, haben wir überwiegend (angehende) Akademiker und Selbstständige/Unternehmer in unserem Bestand. Daher ist unsere Zielgruppe eher im 'gebildeten Bereich' zu suchen, ohne groß wertend klingen zu wollen. Die Altersspanne liegt vermehrt zwischen 25-45 jahren.
Neben den Akademikern und den Unternehmern betreuen wir zunehmend Klein- und Mittelständische Unternehmen im Bereich 'Betriebliches Vorsorgemanagement'.
--> Kurz gesagt: (Angehende) Akademiker, Selbstständige/Unternehmer, Klein- & Mittelständische Unternehmen
Wer wir sind:
Ein überwiegend junges und dynamisches Team aus 12 Leuten im Alter zwischen 22 und 38. Lediglich unser 'Senior' hat so gerade die 40er-Marke übersprungen. Jeder von uns ist hoch motiviert stets die optimale Lösung für seine Mandanten herauszuarbeiten.
Aufgabenstellung
Nach 14 Jahren bei der 'lumavent GmbH Makler', werden wir uns nun mit einem Teil des Teams "abspalten" und die 'lumavent capital partners' gründen.
Uns ist wichtig, dass mit dem Logo ein frischer Wind einhergeht und eine "Novation" zu erkennen ist. Dennoch soll weiterhin zu erkennen sein, dass wir nach wie vor im gleichen Sektor tätig sind und der Bruch nicht zu radikal ist.
Wir wollen also gerne nach wie vor als "lumavent" wahrgenommen werden, aber mit dem Logo muss klar werden, dass wir nicht mehr die alte "lumavent" sind. Diese wird nämlich nach wie vor bestehen bleiben, aber an anderen Standorten und mit leicht anderen Schwerpunkten ihre Mandaten beraten.
Wir werden in Hannover, Paderborn, Kassel und im Sauerland aktiv sein. Die alte lumavent in Köln, Magdeburg und Jena. Die Lösung wird also ein kleiner Drahtseilakt ;-)
Evtl. können Teile des alten Schriftzugs erhalten bleiben und mit neuer Farbe und dem Zusatz "financial services" verknüpft werden (Altes Logo ist beigefügt).
Die Farbe grün wird doch als neu und frisch wahrgenommen, oder?!
Wir sind aber auch gerne offen für alle anderen Ideen!!!

```html
<!DOCTYPE html>
<html lang="de">
<head>
<meta charset="utf-8">
<title>lumavent capital partners – Geschäftsausstattung</title>
<link href="https://fonts.googleapis.com/css2?family=Questrial&display=swap" rel="stylesheet">
<style>
:root{
  --green:#a6c814;
  --green-faint:#f3f8e2;
  --dark:#3c3c3c;
  --paper:#ffffff;
  --bg:#efefef;
  --window:#a9a9a9;
}
*{margin:0;padding:0;box-sizing:border-box}
html,body{width:1200px;height:801px;overflow:hidden}
body{background:var(--bg);font-family:"Questrial",sans-serif;color:var(--dark);position:relative}

.piece{position:absolute;background:var(--paper);overflow:hidden}

.logo{position:absolute;display:flex;align-items:center;gap:calc(var(--s)*0.3)}
.logo-mark{width:calc(var(--s)*1.25);height:calc(var(--s)*1.25);border-radius:50%;background:var(--green);flex:none}
.logo-text{color:var(--dark);line-height:1}
.logo-name{display:block;font-size:var(--s);letter-spacing:-0.01em}
.logo-sub{display:block;font-size:calc(var(--s)*0.43);margin-top:calc(var(--s)*0.06)}

.hero-logo{left:171px;top:95px;--s:62px}

.card-front{left:57px;top:254px;width:260px;height:167px}
.card-front .logo{left:64px;top:62px;--s:26px}

.card-back{left:333px;top:254px;width:260px;height:168px}
.card-back .logo{left:38px;top:23px;--s:26px}
.card-band{position:absolute;left:0;right:0;top:82px;bottom:0;background:var(--dark);color:#fff;font-size:7.3px}
.card-col{position:absolute;top:20px;line-height:13px}
.card-col.left{left:38px}
.card-col.right{left:123px}

.envelope{left:58px;top:496px;width:537px;height:267px}
.envelope .logo{left:49px;top:46px;--s:28px}
.env-window{position:absolute;left:47px;top:121px;width:206px;height:111px;border-radius:12px;background:linear-gradient(135deg,#9c9c9c,#b4b4b4)}

.letterhead{left:630px;top:34px;width:521px;height:737px;font-size:7px;line-height:10.4px}
.letterhead .logo{left:363px;top:45px;--s:24px}
.fold{position:absolute;left:0;width:7px;height:1px;background:var(--dark)}
.sender-line{position:absolute;left:62px;top:156px;font-size:5.6px}
.recipient{position:absolute;left:62px;top:168px;font-size:8.2px;line-height:12.2px}
.contact{position:absolute;right:33px;top:135px;text-align:right;font-size:6.6px}
.contact p+p{margin-top:7px}
.subject{position:absolute;left:62px;top:245px}
.body-copy{position:absolute;left:62px;top:277px;width:430px}
.body-copy p{margin-bottom:10.4px}
.deco-circle{position:absolute;left:309px;top:485px;width:178px;height:178px;border-radius:50%;background:var(--green-faint)}
.footer{position:absolute;left:0;right:0;top:661px;bottom:0;background:var(--dark);color:#fff;font-size:6.4px}
.footer-col{position:absolute;top:23px}
</style>
</head>
<body>

<div class="logo hero-logo">
  <span class="logo-mark"></span>
  <span class="logo-text"><span class="logo-name">lumavent</span><span class="logo-sub">capital partners</span></span>
</div>

<section class="piece card-front">
  <div class="logo"><span class="logo-mark"></span><span class="logo-text"><span class="logo-name">lumavent</span><span class="logo-sub">capital partners</span></span></div>
</section>

<section class="piece card-back">
  <div class="logo"><span class="logo-mark"></span><span class="logo-text"><span class="logo-name">lumavent</span><span class="logo-sub">capital partners</span></span></div>
  <div class="card-band">
    <div class="card-col left">lumavent<br>Lindenweg 14<br>30159 Hannover<br>www.lumavent-cp.de</div>
    <div class="card-col right">LENA HOFBAUER<br>Position<br>l.hofbauer@lumavent.de<br>Tel.: 0511 730294</div>
  </div>
</section>

<section class="piece envelope">
  <div class="logo"><span class="logo-mark"></span><span class="logo-text"><span class="logo-name">lumavent</span><span class="logo-sub">capital partners</span></span></div>
  <div class="env-window"></div>
</section>

<section class="piece letterhead">
  <div class="logo"><span class="logo-mark"></span><span class="logo-text"><span class="logo-name">lumavent</span><span class="logo-sub">capital partners</span></span></div>
  <span class="fold" style="top:261px"></span>
  <span class="fold" style="top:369px"></span>
  <span class="fold" style="top:522px"></span>

  <div class="sender-line">lumavent capital partners | Lindenweg 14 | 30159 Hannover</div>
  <div class="recipient">Herr Albrecht<br>Gartenstraße 7<br>33098 Paderborn</div>

  <div class="contact">
    <p>lumavent capital partners<br>Lindenweg 14<br>30159 Hannover</p>
    <p>Telefon: 0511 730294<br>Telefax: 0511 730295</p>
    <p>info@lumavent-cp.de<br>www.lumavent-cp.de</p>
  </div>

  <div class="subject">Hier steht eine Betreffzeile</div>

  <div class="body-copy">
    <p>Sehr geehrte Frau Albrecht,</p>
    <p>als Kunde unseres jungen und modernen Unternehmens erwartet<br>Sie Qualität in höchstem Maße.</p>
    <p>Sie können sicher zu sein, genau zu bekommen, was wir Ihnen versprechen.<br>Und damit werden Sie auch rundum zufrieden sein. Das garantieren wir Ihnen.</p>
    <p>Schauen Sie doch gleich das beiliegende Prospekt. Wir bieten Ihnen moderne und hochwertige Produkte, die auf dem neuesten Stand der Technik sind, an. Überzeugen Sie sich selbst von der hochwertigen Qualität unserer Produkte und bestellen Sie noch heute.</p>
    <p>Wir freuen uns auf Ihre Bestellung und sind bei Rückfragen gerne für Sie da.</p>
    <p>Mit freundlichen Grüßen</p>
  </div>

  <div class="deco-circle"></div>

  <footer class="footer">
    <div class="footer-col" style="left:50px">lumavent capital partners<br>Lindenweg 14<br>30159 Hannover</div>
    <div class="footer-col" style="left:189px">USt-IDNR: DE4417725<br>Steuernummer: 217/455/108<br>Inhaber: Lena Hofbauer</div>
    <div class="footer-col" style="left:365px">Stadtsparkasse Nordland<br>IBAN: DE27 2505 0000 0000 4471<br>BIC: NORLDEXX31</div>
  </footer>
</section>

</body>
</html>
```